Business Card Design Project

Looking to have a new business card created.

The card needs to be sort of two cards attached in the centre creating a flip card so we can write in the centre.

First side with my information at the director / licensee and then the back side with my assistant's details.

Inside with minimal information, facebook link/sign and then lines to write on.

www.norlandestates.com.au is my website to show colours and designs that I like.

Target Market(s)

Property Owners, Property Investors, Tenants, rental clients, Tradesman.

Industry/Entity Type

Business

Requirements
Must have
• Professional & symmetrical.

Am getting pro photos for myself & assistance, so a space for these once received.

```html
<!DOCTYPE html>
<html lang="en">
<head>
<meta charset="utf-8">
<title>Norland Estates – Flip Card Layout</title>
<link rel="stylesheet" href="https://fonts.googleapis.com/css2?family=Source+Sans+3:wght@400;600;700&display=swap">
<style>
  :root{
    --page:#eceded;
    --label:#333;
    --card-deep:#061419;
    --card-mid:#0c2a35;
    --card-glow:#1b4a58;
    --band-light:#b7d0dc;
    --band-dark:#6b8e9e;
    --text:#ffffff;
    --brand:#8fb0c0;
    --frame:#8db4c6;
    --photo-text:#9bb4bf;
    --social:#6f93a3;
    --rule:#2b4a60;
    --note:#ffffff;
  }
  *{margin:0;padding:0;box-sizing:border-box}
  html,body{width:1200px;height:829px;overflow:hidden;background:var(--page)}
  body{position:relative;font-family:"Source Sans 3",Arial,sans-serif;color:var(--text)}
  .section-label{position:absolute;color:var(--label);font-size:17px}
  .section-label--inside{font-size:24px}
  .card{
    position:absolute;width:556px;height:326px;overflow:hidden;
    background:
      radial-gradient(ellipse 60% 30% at 55% 12%,rgba(60,120,140,.35),transparent 70%),
      radial-gradient(ellipse 45% 40% at 20% 60%,rgba(30,80,95,.35),transparent 70%),
      linear-gradient(165deg,var(--card-glow) 0%,var(--card-mid) 35%,var(--card-deep) 100%);
  }
  .brand{position:absolute;left:56px;top:40px;font-size:34px;font-weight:400;color:var(--brand);letter-spacing:.5px;display:flex;align-items:center;gap:10px}
  .brand-mark{width:14px;height:14px;background:var(--brand)}
  .band{position:absolute;left:0;width:100%;height:29px;
    background:linear-gradient(180deg,var(--band-light) 0%,var(--band-dark) 55%,#4d7282 100%)}
  .photo-slot{position:absolute;left:387px;top:58px;width:111px;height:140px;border:2px solid var(--frame);
    background:linear-gradient(160deg,#1d4654,#0a2029);display:flex;justify-content:center;padding-top:48px;
    color:var(--photo-text);font-weight:700;font-size:24px}
  .person-name{position:absolute;left:60px;top:122px;font-size:24px;font-weight:700;letter-spacing:.5px}
  .role{position:absolute;left:60px;font-size:18px;line-height:25px}
  .contacts{position:absolute;left:60px;list-style:none;font-size:18px;line-height:24px}
  .contacts li{display:flex;align-items:center;gap:12px}
  .contacts .strong{font-weight:700}
  .contacts svg{width:12px;height:12px;flex:none}
  .site-url{position:absolute;left:37px;top:125px;font-size:15px;font-weight:700;letter-spacing:.3px}
  .social{position:absolute;top:46px;left:407px;display:flex;gap:2px}
  .social span{width:44px;height:44px;border-radius:7px;background:var(--social)}
  .inside-info{position:absolute;left:39px;top:171px;font-size:17px;line-height:26.5px}
  .inside-info .strong{font-weight:700}
  .acn{position:absolute;right:26px;top:283px;font-size:13px}
  .note-panel{position:absolute;left:24px;top:29px;width:502px;height:270px;background:var(--note);border:1px solid #9fb4c0}
  .note-line{position:absolute;left:19px;width:468px;height:1px;background:var(--rule)}
</style>
</head>
<body>
  <div class="section-label" style="left:39px;top:14px">Front</div>
  <div class="section-label" style="left:608px;top:13px">Back</div>
  <div class="section-label section-label--inside" style="left:58px;top:428px">Inside</div>

  <!-- Front: director -->
  <section class="card" style="left:36px;top:49px">
    <div class="brand"><span>Norland Estates</span></div>
    <div class="band" style="top:118px"></div>
    <div class="photo-slot" role="img" aria-label="Space for director's portrait photo">Photo</div>
    <div class="person-name">CLAIRE DONOVAN</div>
    <div class="role" style="top:150px">Managing Director<br>Principal REA</div>
    <ul class="contacts" style="top:212px">
      <li class="strong"><svg viewBox="0 0 12 12"><path d="M2 1l2 0 1 3-1.5 1a6 6 0 0 0 3 3L8 6.5l3 1v2L9.5 11A9 9 0 0 1 1 2.5z" fill="#fff"/></svg>1300 555 214</li>
      <li class="strong"><svg viewBox="0 0 12 12"><rect x="3" y="1" width="6" height="10" rx="1" fill="none" stroke="#fff"/></svg>0400 555 118</li>
      <li><svg viewBox="0 0 12 12"><rect x="1" y="2.5" width="10" height="7" fill="none" stroke="#fff"/><path d="M1 2.5l5 4 5-4" fill="none" stroke="#fff"/></svg>claire@norlandestates.com.au</li>
    </ul>
  </section>

  <!-- Back: assistant -->
  <section class="card" style="left:606px;top:49px">
    <div class="brand"><span>Norland Estates</span></div>
    <div class="band" style="top:118px"></div>
    <div class="photo-slot" role="img" aria-label="Space for rental manager's portrait photo">Photo</div>
    <div class="person-name">PETRA LINDQVIST</div>
    <div class="role" style="top:158px">Rental Manager</div>
    <ul class="contacts" style="top:204px">
      <li class="strong"><svg viewBox="0 0 12 12"><path d="M2 1l2 0 1 3-1.5 1a6 6 0 0 0 3 3L8 6.5l3 1v2L9.5 11A9 9 0 0 1 1 2.5z" fill="#fff"/></svg>1300 555 214</li>
      <li><svg viewBox="0 0 12 12"><rect x="1" y="2.5" width="10" height="7" fill="none" stroke="#fff"/><path d="M1 2.5l5 4 5-4" fill="none" stroke="#fff"/></svg>petra@norlandestates.com.au</li>
    </ul>
  </section>

  <!-- Inside: company details -->
  <section class="card" style="left:36px;top:469px">
    <div class="brand" style="left:36px;top:32px"><span>Norland Estates</span></div>
    <div class="social" aria-label="Social media links"><span></span><span></span></div>
    <div class="band" style="top:120px"></div>
    <div class="site-url">WWW.NORLANDESTATES.COM.AU</div>
    <div class="inside-info">
      <div class="strong">Apply online: http://bit.ly/norlandes</div>
      <div class="strong">1300 OUR NOR</div>
      <div>Postal Address: PO Box 417, Harbourton Q 4099</div>
      <div>Office Location: Level 2/58 Seaview Parade, Harbourton Q 4099</div>
    </div>
    <div class="acn">ACN: 000 111 222</div>
  </section>

  <!-- Inside: note lines -->
  <section class="card" style="left:606px;top:469px">
    <div class="note-panel">
      <div class="note-line" style="top:55px"></div>
      <div class="note-line" style="top:101px"></div>
      <div class="note-line" style="top:141px"></div>
      <div class="note-line" style="top:181px"></div>
      <div class="note-line" style="top:224px"></div>
    </div>
  </section>
</body>
</html>
```